KWT Contracting services . Building and maintenance services, optic fibre installation

Business cards and logo design.I need a logo that I can use on business cards ,workwear and on my vehicles. I would like the KWT to be the main or larger text and contracting services to be the smaller or less important text.I like monograms, modern designs and repeating patterns symbols. I am also a Gemini and my favourite number is 22 so if this can be any inspiration to help with the design. Am thinking of the using German flag colours as a his is my family’s heritage. And the other 2 main colours I wear is black and white.But any ideas are appreciated.I do not need a design that is trade specific but a design that could be used for any business.

Target Market(s)

General public

Contact Information for Business Card

KWT Contracting Services ( front of business card)

(Back of business card)
Milo Brackwood
0471539264
Maintenance services
Optic fibre and data installation

Logo Text

Logo can just be pattern or monogram or incorporate KWT . I like the gemini star sign and the number 22

Colors
ec1f27
000000
fbee3e
ffffff

Requirements
Must have
• Logo and KWT Contracting Services on the front of business card
Nice to have
• Possible use of German flag colours.
• Modern design.
• Design to be able to be used on black or white background as I want to put it on clothing

```html
<!DOCTYPE html>
<html lang="en">
<head>
<meta charset="utf-8">
<title>KWT Contracting Services – Business Card</title>
<link href="https://fonts.googleapis.com/css2?family=Lato:wght@300;400;900&display=swap" rel="stylesheet">
<style>
  :root {
    --brand-red: #e11d26;
    --brand-yellow: #f2c200;
    --ink: #1a1a1a;
    --card-white: #ffffff;
    --card-black: #050505;
    --stage: #2b2b2b;
    --soft-white: #f1f1f1;
  }
  * { box-sizing: border-box; margin: 0; padding: 0; }
  html, body { width: 1200px; height: 900px; overflow: hidden; }
  body {
    background: var(--stage);
    font-family: "Lato", Arial, sans-serif;
    display: flex;
    flex-direction: column;
    align-items: center;
    justify-content: center;
    gap: 50px;
  }
  .card {
    position: relative;
    width: 630px;
    height: 360px;
    border-radius: 20px;
    overflow: hidden;
  }
  /* Front (white) */
  .card--front { background: linear-gradient(135deg, #ffffff 0%, #f4f4f4 60%, #e6e6e6 100%); color: var(--ink); }
  .holder { position: absolute; left: 44px; top: 48px; }
  .holder__name {
    color: var(--brand-red);
    font-size: 30px;
    font-weight: 400;
    letter-spacing: 0.5px;
    text-transform: uppercase;
  }
  .holder__title { font-size: 17px; margin-top: 2px; }
  .divider {
    position: absolute;
    left: 150px; top: 118px;
    width: 300px; height: 2px;
    background: var(--ink);
  }
  .contacts { position: absolute; left: 44px; top: 130px; list-style: none; }
  .contacts li {
    display: flex; align-items: center; gap: 10px;
    font-size: 16px; line-height: 24px;
  }
  .contacts svg { width: 12px; height: 12px; flex: none; }
  .logo-name {
    position: absolute;
    display: flex; align-items: flex-start; gap: 10px;
    font-weight: 900;
    color: var(--brand-red);
  }
  .logo-name__mark { width: 18px; height: 18px; background: var(--brand-yellow); margin-top: 10px; }
  .logo-name__main { display: block; line-height: 0.9; }
  .logo-name__sub { display: block; text-transform: uppercase; letter-spacing: 1px; }
  .card--front .logo-name { right: 50px; top: 110px; }
  .card--front .logo-name__main { font-size: 96px; }
  .card--front .logo-name__sub { font-size: 17px; margin-top: 6px; }
  .address {
    position: absolute; right: 44px; bottom: 40px;
    text-align: right; font-size: 17px; line-height: 24px;
  }
  /* Back (black) */
  .card--back { background: var(--card-black); color: var(--soft-white); }
  .card--back .logo-name { left: 50%; top: 60px; transform: translateX(-50%); }
  .card--back .logo-name__main { font-size: 110px; }
  .card--back .logo-name__sub { font-size: 19px; margin-top: 6px; }
  .services {
    position: absolute; left: 0; right: 0; top: 235px;
    text-align: center; text-transform: uppercase;
    font-weight: 300; letter-spacing: 2px; font-size: 18px; line-height: 28px;
  }
  .services__lead { color: var(--brand-yellow); }
</style>
</head>
<body>
  <section class="card card--front" aria-label="Business card front">
    <div class="holder">
      <p class="holder__name">Milo Brackwood</p>
      <p class="holder__title">Director</p>
    </div>
    <div class="divider"></div>
    <ul class="contacts">
      <li>
        <svg viewBox="0 0 12 12" aria-hidden="true"><path d="M2 1h3l1 3-2 1a7 7 0 0 0 3 3l1-2 3 1v3c-6 0-9-3-9-9z" fill="var(--brand-red)"/></svg>
        0471539264
      </li>
      <li>
        <svg viewBox="0 0 12 12" aria-hidden="true"><rect x="1" y="2.5" width="10" height="7" fill="none" stroke="var(--brand-red)" stroke-width="1.2"/><path d="M1 2.5l5 4 5-4" fill="none" stroke="var(--brand-red)" stroke-width="1.2"/></svg>
        KWT@brackwoodworks.com
      </li>
      <li>
        <svg viewBox="0 0 12 12" aria-hidden="true"><circle cx="6" cy="6" r="5" fill="none" stroke="var(--brand-red)" stroke-width="1.2"/><path d="M1 6h10M6 1c-3 3-3 7 0 10M6 1c3 3 3 7 0 10" fill="none" stroke="var(--brand-red)" stroke-width="1"/></svg>
        www.brackwoodworks.com
      </li>
    </ul>
    <div class="logo-name">
      <span class="logo-name__mark"></span>
      <span>
        <span class="logo-name__main">KWT</span>
        <span class="logo-name__sub">Contracting Services</span>
      </span>
    </div>
    <address class="address" style="font-style:normal">
      18 Larkspur Row,<br>
      Millbrook, FL 32990, USA
    </address>
  </section>

  <section class="card card--back" aria-label="Business card back">
    <div class="logo-name">
      <span class="logo-name__mark"></span>
      <span>
        <span class="logo-name__main">KWT</span>
        <span class="logo-name__sub">Contracting Services</span>
      </span>
    </div>
    <div class="services">
      <p class="services__lead">Maintenance Services</p>
      <p>Optic Fibre and Data Installation</p>
    </div>
  </section>
</body>
</html>
```